CalmHarbor Homepage and Landing Pages

Please see detailed brief.

CalmHarbor is Australia’s newest online therapy and mental health service. We allow patients from across australia to connect with Mental health practitioners from across Australia. Our mission is to remove the friction in gaining support for mental health related issues.

Number of Pages Required

1 page

Font styles to use
Sans Serif

Colors
33a6d7
0293ce
3277b5
0255a3
acd136
9bcb3c

Requirements
Must have
• Please see detailed brief.
Nice to have
• Please see detailed brief
Should not have

```html
<!DOCTYPE html>
<html lang="en">
<head>
<meta charset="utf-8">
<title>CalmHarbor — Online Therapy</title>
<link href="https://fonts.googleapis.com/css2?family=Poppins:wght@300;400;500;600&display=swap" rel="stylesheet">
<style>
  :root{
    --sky:#33a6d7;
    --ocean:#0293ce;
    --steel:#3277b5;
    --navy:#0255a3;
    --lime:#acd136;
    --leaf:#9bcb3c;
    --ink:#2f2f33;
    --text:#555a60;
    --muted:#777c82;
    --rule:#e4e6e8;
    --pale:#eef7fc;
    --footer:#222326;
    --white:#ffffff;
  }
  *{margin:0;padding:0;box-sizing:border-box}
  html,body{width:1200px;height:2630px;overflow:hidden}
  body{position:relative;font-family:'Poppins',sans-serif;color:var(--text);background:var(--white)}
  .abs{position:absolute}
  .btn{position:absolute;display:flex;align-items:center;justify-content:center;color:var(--white);
       font-size:13px;font-weight:500;background:linear-gradient(90deg,var(--leaf),var(--sky));text-transform:uppercase}

  /* header */
  .site-header{left:0;top:0;width:1200px;height:96px;background:var(--white);border-bottom:1px solid var(--rule)}
  .brand{left:111px;top:26px;display:flex;align-items:center;gap:12px;font-size:36px;font-weight:400;color:var(--ink)}
  .brand-dot{width:28px;height:28px;border-radius:50%;background:var(--ocean)}
  .nav{left:500px;top:44px;display:flex;gap:41px;font-size:12.5px;font-weight:500;color:#3a3d42;text-transform:uppercase}
  .nav .active{color:var(--navy)}

  /* hero */
  .hero{left:0;top:96px;width:1200px;height:633px;
        background:linear-gradient(100deg,#f4f6f8 0%,#e9ecef 30%,#c9b7a6 55%,#8c7868 75%,#4d6270 100%)}
  .hero-title{left:111px;top:220px;font-size:51px;font-weight:500;color:var(--navy)}
  .hero-text{left:111px;top:294px;width:330px;font-size:13px;line-height:26.5px;color:#444}
  .hero-btn{left:111px;top:366px;width:105px;height:38px;font-size:12.5px}

  /* profile card */
  .profile{left:111px;top:551px;width:978px;height:518px;background:var(--white);box-shadow:0 2px 10px rgba(0,0,0,.12)}
  .profile-photo{left:40px;top:42px;width:367px;height:434px;background:linear-gradient(160deg,#2a2a2c,#141416 60%,#2c3140)}
  .profile-name{left:455px;top:74px;font-size:26px;font-weight:500;color:var(--ink)}
  .profile-role{left:455px;top:116px;font-size:17px;color:var(--leaf)}
  .profile-bio{left:456px;top:166px;width:458px;font-size:12.5px;line-height:25.7px;color:var(--text);text-align:justify}
  .profile-bio p+p{margin-top:25.7px}
  .profile-btn{left:458px;top:416px;width:121px;height:39px}

  /* how it works */
  .section-title{left:0;width:1200px;text-align:center}
  .how-title{top:1126px;font-size:34px;color:var(--ink);font-weight:400}
  .how-sub{top:1184px;font-size:13px;color:var(--muted)}
  .step{top:1248px;width:280px}
  .step svg{display:block;height:52px}
  .step h3{margin-top:22px;font-size:17px;font-weight:500;color:var(--ocean)}
  .step p{margin-top:12px;font-size:13px;line-height:26px;color:#444}
  .divider{top:1255px;width:1px;height:202px;background:var(--rule)}
  .how-btn{left:534px;top:1476px;width:132px;height:42px;font-size:14px;text-transform:none}
  .how-btn span{text-transform:uppercase}

  /* band */
  .band{left:0;top:1557px;width:1200px;height:488px;background:linear-gradient(100deg,var(--lime) 0%,#7fc48a 40%,#44a9c8 75%,var(--ocean) 100%)}
  .band-text{left:0;top:1605px;width:1200px;text-align:center;font-size:23px;line-height:43px;color:var(--white);font-weight:300}
  .partner{top:1738px;width:152px;height:46px;border-radius:6px;background:rgba(255,255,255,.85)}
  .lower{left:0;top:2045px;width:1200px;height:526px;background:var(--pale)}

  /* testimonials */
  .quote-card{top:1871px;width:311px;height:335px;background:var(--white);box-shadow:0 2px 8px rgba(0,0,0,.1);text-align:center;padding:0 28px}
  .quote-mark{margin-top:18px;height:50px;font-size:72px;line-height:80px;color:var(--leaf);font-weight:300}
  .quote-card h4{margin-top:10px;font-size:20px;font-weight:400;color:var(--ink)}
  .quote-card p{margin-top:12px;font-size:13px;line-height:25.7px;color:var(--muted);text-align:justify;text-align-last:center}
  .quote-name{margin-top:16px;font-size:13px;font-weight:500;color:var(--ink)}
  .quote-role{margin-top:2px;font-size:11px;color:var(--muted)}

  /* call to action */
  .cta-dot{left:582px;top:2260px;width:36px;height:36px;border-radius:50%;background:var(--ocean)}
  .cta-name{top:2310px;font-size:66px;color:var(--ink);font-weight:400}
  .cta-line{top:2406px;font-size:24px;color:#3a3d42}
  .cta-btn{left:511px;top:2469px;width:179px;height:43px;font-size:15px;text-transform:none}

  .site-footer{left:0;top:2571px;width:1200px;height:59px;background:var(--footer);color:var(--white);
               font-size:12px;font-weight:500;display:flex;align-items:center;justify-content:center}
</style>
</head>
<body>

<header class="abs site-header">
  <div class="abs brand"><span class="brand-dot"></span>CalmHarbor</div>
  <nav class="abs nav">
    <span class="active">Home</span><span>About Us</span><span>Our Team</span><span>Practitioner Information</span><span>Contact Us</span>
  </nav>
</header>

<section class="abs hero" role="img" aria-label="Smiling practitioner with blonde hair talking with a patient in a bright clinic room"></section>
<h1 class="abs hero-title">CalmHarbor</h1>
<p class="abs hero-text">Sed ut perspiciatis unde omnis iste natus error sit voluptatem accusantium doloremque</p>
<a class="btn hero-btn">Read More</a>

<section class="abs profile">
  <div class="abs profile-photo" role="img" aria-label="Portrait of the chief science advisor in a dark jacket"></div>
  <h2 class="abs profile-name">Dr. Alan Kerwick</h2>
  <div class="abs profile-role">Neuroscientist &amp; Chief Science Advisor</div>
  <div class="abs profile-bio">
    <p>Dr Alan Kerwick is an Australian neuroscientist in private practice specializing in brain performance. He has a bachelor's degree in psychology and a doctorate of science in biological statistics. Dr Kerwick has worked as a psychologist for over 30 years and more recently has focused on the neurosciences.</p>
    <p>Alan has helped many people, schools, sporting teams and organisations with improving performance and in particular memory, concentration, agility and resilience. It was through the discovery of the positive</p>
  </div>
  <a class="btn profile-btn">Read More</a>
</section>

<h2 class="abs section-title how-title">How it Works</h2>
<p class="abs section-title how-sub">CalmHarbor provides on demand access to highly qualified physicians from across Australia.</p>

<div class="abs step" style="left:111px">
  <svg viewBox="0 0 44 52" width="44" fill="none" stroke="#2d3b55" stroke-width="1.6">
    <circle cx="22" cy="14" r="10"/><path d="M3 50v-10c0-8 8-12 19-12s19 4 19 12v10z"/><path d="M15 29v10M29 29v10"/><circle cx="15" cy="42" r="3" stroke="var(--ocean)"/>
  </svg>
  <h3>Find a Practitoner</h3>
  <p>Search for health professional that best suits your circumstances from anywhere in Australia.</p>
</div>
<div class="abs divider" style="left:416px"></div>
<div class="abs step" style="left:466px">
  <svg viewBox="0 0 46 52" width="46" fill="none" stroke="#2d3b55" stroke-width="1.6">
    <rect x="2" y="8" width="42" height="42" rx="3"/><path d="M12 3v10M34 3v10M2 18h42"/>
    <g fill="var(--ocean)" stroke="none"><rect x="9" y="25" width="5" height="4"/><rect x="18" y="25" width="5" height="4"/><rect x="27" y="25" width="5" height="4"/><rect x="9" y="34" width="5" height="4"/><rect x="18" y="34" width="5" height="4"/><rect x="27" y="34" width="5" height="4"/><rect x="36" y="34" width="5" height="4"/></g>
  </svg>
  <h3>Book an Appointment</h3>
  <p>Book an online appointment at at time that suits you.24/7 and 356 days a year.</p>
</div>
<div class="abs divider" style="left:767px"></div>
<div class="abs step" style="left:822px">
  <svg viewBox="0 0 60 52" width="60" fill="none" stroke="#2d3b55" stroke-width="1.6">
    <rect x="18" y="2" width="26" height="14" rx="2" stroke="var(--ocean)"/><path d="M24 16l-3 5 7-5"/>
    <circle cx="16" cy="30" r="6"/><path d="M3 50v-5c0-5 6-8 13-8s13 3 13 8v5z"/>
    <circle cx="44" cy="30" r="6"/><path d="M31 50v-5c0-5 6-8 13-8s13 3 13 8v5z"/>
  </svg>
  <h3>Chat with your consultant</h3>
  <p>When it's time for your consultation, simply log in and start your sessionYou have the option of conducting</p>
</div>
<a class="btn how-btn"><span>Read More</span></a>

<section class="abs band" role="img" aria-label="Soft green to blue tinted photo of a therapy session"></section>
<section class="abs lower"></section>
<p class="abs band-text">CalmHarbor provides on-demand access to a range of<br>psychologists &amp; personal wellness professionals from across Australia.</p>
<div class="abs partner" style="left:202px"></div>
<div class="abs partner" style="left:412px"></div>
<div class="abs partner" style="left:627px"></div>
<div class="abs partner" style="left:846px"></div>

<article class="abs quote-card" style="left:111px">
  <div class="quote-mark">“</div>
  <h4>Nemo enim ipsam</h4>
  <p>Sed ut perspiciatis unde omnis iste nat us error sit voluptatem accusantium dolor emque laudantium, totam rem aperiam, eaque ipsa quae ab illo inven vitae dicta sunt explicabo.</p>
  <div class="quote-name">JHON SMITH</div>
  <div class="quote-role">Mental Therpahy Doctors</div>
</article>
<article class="abs quote-card" style="left:445px">
  <div class="quote-mark">“</div>
  <h4>Nemo enim ipsam</h4>
  <p>Sed ut perspiciatis unde omnis iste nat us error sit voluptatem accusantium dolor emque laudantium, totam rem aperiam, eaque ipsa quae ab illo inven vitae dicta sunt explicabo.</p>
  <div class="quote-name">JHON SMITH</div>
  <div class="quote-role">Mental Therpahy Doctors</div>
</article>
<article class="abs quote-card" style="left:778px">
  <div class="quote-mark">“</div>
  <h4>Nemo enim ipsam</h4>
  <p>Sed ut perspiciatis unde omnis iste nat us error sit voluptatem accusantium dolor emque laudantium, totam rem aperiam, eaque ipsa quae ab illo inven vitae dicta sunt explicabo.</p>
  <div class="quote-name">JHON SMITH</div>
  <div class="quote-role">Mental Therpahy Doctors</div>
</article>

<div class="abs cta-dot"></div>
<div class="abs section-title cta-name">CalmHarbor</div>
<p class="abs section-title cta-line">Book your online appointment in minutes, 24/7.</p>
<a class="btn cta-btn">Find a Practitioner</a>

<footer class="abs site-footer">© Copyrights 2020-CalmHarbor.All Rights Reserved.</footer>

</body>
</html>
```